Minimalist Modern Business Card Design, open to ideas, or cleaner version of provided files, but what logo & logo colors (with some black) as shown in files, and info for back shown in files as well.

```html
<!DOCTYPE html>
<html lang="en">
<head>
<meta charset="utf-8">
<title>Roadline Fleet Works — Business Card</title>
<link rel="stylesheet" href="https://fonts.googleapis.com/css2?family=Montserrat:wght@500;600&family=Source+Sans+3:wght@400;600;700&display=swap">
<style>
  :root {
    --ink: #1a1a14;
    --brand: #332f66;
    --navy: #1e1a5c;
    --text: #2b2b2b;
    --card: #ffffff;
    --backdrop: #e6e6e8;
    --map: #f1f1f3;
  }
  * { margin: 0; padding: 0; box-sizing: border-box; }
  html, body { width: 1200px; height: 789px; overflow: hidden; }
  body {
    background: var(--backdrop);
    font-family: "Source Sans 3", Arial, sans-serif;
    color: var(--text);
    position: relative;
  }
  .card {
    position: absolute;
    top: 230px;
    width: 560px;
    height: 330px;
    background: var(--card);
    box-shadow: 6px 8px 14px rgba(0,0,0,.28);
    overflow: hidden;
  }
  .card--front { left: 25px; }
  .card--back { left: 615px; }
  .card__shapes { position: absolute; inset: 0; width: 100%; height: 100%; }

  .brand {
    position: absolute; left: 34px; top: 82px;
    display: flex; align-items: center; gap: 14px;
  }
  .brand__square { width: 40px; height: 40px; background: var(--brand); }
  .brand__name {
    font-family: "Montserrat", Arial, sans-serif;
    font-weight: 600; font-size: 25px; line-height: 26px;
    color: var(--brand);
  }
  .person { position: absolute; left: 33px; top: 156px; }
  .person__name { font-size: 24px; font-weight: 400; color: #2a2d3a; line-height: 1; }
  .person__name strong { font-weight: 700; }
  .person__role { font-size: 13.5px; margin-top: 4px; }

  .contact { position: absolute; left: 33px; top: 252px; font-size: 11px; }
  .contact__row { display: flex; align-items: center; gap: 20px; margin-top: 10px; }
  .contact__item { display: flex; align-items: center; gap: 7px; }
  .contact__item svg { width: 15px; height: 15px; fill: var(--brand); }

  .map {
    position: absolute; left: 250px; top: 55px; width: 250px; height: 200px;
    background: radial-gradient(ellipse at center, var(--map) 0%, rgba(241,241,243,0) 72%);
  }
  .services { position: absolute; top: 38px; }
  .services--left { left: 33px; }
  .services--right { left: 290px; }
  .services__title { font-size: 13.5px; font-weight: 700; color: var(--brand); letter-spacing: .2px; }
  .services__list {
    margin-top: 8px; padding-left: 22px;
    font-size: 14px; line-height: 17.5px; color: var(--brand);
  }
  .services--left .services__list { width: 240px; }
</style>
</head>
<body>

<section class="card card--front" aria-label="Business card front">
  <svg class="card__shapes" viewBox="0 0 637 375" preserveAspectRatio="none" aria-hidden="true">
    <polygon points="0,0 390,0 420,46 0,46" fill="var(--ink)"/>
    <polygon points="397,0 637,0 637,82 457,82" fill="var(--brand)"/>
    <polygon points="30,250 288,250 300,264 30,264" fill="var(--ink)"/>
    <rect x="312" y="259" width="294" height="4" fill="var(--navy)"/>
  </svg>
  <div class="brand">
    <span class="brand__square"></span>
    <span class="brand__name">Roadline<br>Fleet Works</span>
  </div>
  <div class="person">
    <p class="person__name"><strong>Name</strong> Surname</p>
    <p class="person__role">President</p>
  </div>
  <div class="contact">
    <p>123 Anywhere St., Any City, ST 12345</p>
    <div class="contact__row">
      <span class="contact__item">
        <svg viewBox="0 0 24 24"><path d="M6.6 10.8a15 15 0 0 0 6.6 6.6l2.2-2.2c.3-.3.7-.4 1-.2 1.1.4 2.3.6 3.6.6.6 0 1 .4 1 1V20c0 .6-.4 1-1 1A17 17 0 0 1 3 4c0-.6.4-1 1-1h3.5c.6 0 1 .4 1 1 0 1.3.2 2.5.6 3.6.1.3 0 .7-.2 1z"/></svg>
        +123-456-7890
      </span>
      <span class="contact__item">
        <svg viewBox="0 0 24 24"><path d="M2 5h20v14H2z M3 6l9 7 9-7" fill="var(--brand)"/><path d="M3 6l9 7 9-7" fill="none" stroke="#fff" stroke-width="1.6"/></svg>
        hello@roadlinefleet.com
      </span>
      <span class="contact__item">
        <svg viewBox="0 0 24 24"><circle cx="12" cy="12" r="9" fill="none" stroke="var(--brand)" stroke-width="2"/><path d="M3 12h18M12 3c3 3 3 15 0 18M12 3c-3 3-3 15 0 18M5 7.5h14M5 16.5h14" fill="none" stroke="var(--brand)" stroke-width="1.4"/></svg>
        www.roadlinefleet.com
      </span>
    </div>
  </div>
</section>

<section class="card card--back" aria-label="Business card back">
  <div class="map" role="img" aria-label="Faint world map backdrop"></div>
  <svg class="card__shapes" viewBox="0 0 637 375" preserveAspectRatio="none" aria-hidden="true">
    <polygon points="30,330 288,330 300,344 30,344" fill="#2e2f3d"/>
    <rect x="312" y="339" width="294" height="4" fill="var(--navy)"/>
  </svg>
  <div class="services services--left">
    <h2 class="services__title">SERVICES INCLUDE</h2>
    <ul class="services__list">
      <li>Shop &amp; Mobile</li>
      <li>DOT &amp; Bit Inspections</li>
      <li>All Maintenance &amp; Repairs</li>
      <li>Check Engine Lights</li>
      <li>Diags, Regens &amp; Programming</li>
      <li>Full Dealer Software Capabilities</li>
      <li>PM &amp; Compliance Tracking</li>
      <li>App-Based Billing &amp; Live Updates</li>
      <li>Dealer Certified Techs</li>
      <li>Night Servicing to Avoid Downtime</li>
    </ul>
  </div>
  <div class="services services--right">
    <h2 class="services__title">SPECIALIZING IN</h2>
    <ul class="services__list">
      <li>Heavy &amp; Medium Duty</li>
      <li>Corvane</li>
      <li>Ikuro</li>
      <li>Hanoma</li>
      <li>Pellworth</li>
      <li>Freightmark</li>
      <li>Kendrick</li>
      <li>Aldermont</li>
      <li>After Treatment</li>
      <li>And more</li>
    </ul>
  </div>
</section>

</body>
</html>
```